Consulting company needs website design

We need a simple, static website design for our consulting company. We are looking for a general design of the look and feel of the website. Initially, it will have these pages:
- Home
- About us
- Services
- Contact us
We have our own logo which I have attached to the brief.

We are looking for a simple website, with white background and the use of gray (darker) as the main theme. Simple fonts. The website should be responsive so it an be easily red in mobile devices.

As part of the project, we will need to receive at least the following items:
- Individual files with sample text to support the pages outlined above
- Necessary CSS files

Our current website is here: http://www.marlowvane.co/

Here are some examples of other website we like to be used as guideline:
- http://www.tornaviamundo.com/
-

Target Market(s)

Individuals and companies looking to hire our company to provide consulting services.

Industry/Entity Type

It Company

Coding

Coded - Design and coding required

Number of Pages Required

4 page

Font styles to use
Sans Serif

Requirements
Must have
• Main page should have the ability to embed Chirply feed into it.
• We prefer the design to use gray tones.

```html
<!DOCTYPE html>
<html lang="en">
<head>
<meta charset="utf-8">
<title>Marlow Vane — Business Consulting</title>
<link rel="stylesheet" href="https://fonts.googleapis.com/css2?family=Fira+Sans:wght@400;500;600;700&family=Open+Sans:ital,wght@0,400;0,600;0,700;1,400&display=swap">
<style>
:root{
  --ink:#2f2f2f;
  --dark:#333333;
  --darker:#262626;
  --band:#3a3a3a;
  --mid:#5a5a5a;
  --muted:#8a8a8a;
  --light:#e6e6e6;
  --paper:#ffffff;
  --accent:#1f4f8f;
  --photo-a:#c9c2b8;
  --photo-b:#6f7686;
}
*{box-sizing:border-box;margin:0;padding:0}
html,body{width:1200px;height:3789px;overflow:hidden;background:var(--paper)}
body{font-family:"Open Sans",Arial,sans-serif;color:var(--ink)}
.page{position:relative;width:1200px;height:3789px;overflow:hidden}
.abs{position:absolute}
.heading{font-family:"Fira Sans",Arial,sans-serif;font-weight:600;text-align:center;position:absolute;left:0;width:1200px}

/* top bar */
.topbar{top:0;left:0;width:1200px;height:38px;background:var(--darker);color:#ddd;font-size:12px}
.topbar .item{position:absolute;top:0;height:38px;display:flex;align-items:center;gap:8px}
.topbar .city{left:1000px;width:152px;background:#555;justify-content:center;font-weight:600;font-size:13px;color:#fff}

/* hero */
.hero{top:38px;left:0;width:1200px;height:588px;background:linear-gradient(110deg,#8f959f 0%,#d8d2c8 35%,#e9e6e1 55%,#6c7486 80%,#3f475a 100%)}
.navbar{top:38px;left:0;width:1200px;height:92px;background:rgba(40,40,40,.82)}
.brand-mark{top:32px;left:52px;width:124px;height:124px;border-radius:50%;background:var(--paper);border:6px solid #555}
.brand-name{top:66px;left:196px;color:#fff;font-family:"Fira Sans",Arial,sans-serif;font-weight:600;font-size:22px;letter-spacing:1px}
.nav{top:38px;left:560px;display:flex;height:92px;align-items:center;gap:0}
.nav a{color:#fff;text-decoration:none;font-family:"Fira Sans",Arial,sans-serif;font-size:14px;font-weight:500;letter-spacing:.5px;padding:0 0 6px;margin-left:56px}
.nav a.active{border-bottom:2px solid #fff;margin-left:30px}
.cta-strip{top:626px;left:0;width:1200px;height:56px;background:var(--light);display:flex;align-items:center}
.cta-strip p{position:absolute;left:48px;font-family:"Fira Sans",Arial,sans-serif;font-size:19px;color:#333}
.cta-strip .btn{position:absolute;left:1032px;top:10px;width:120px;height:36px;background:var(--dark);color:#fff;font-size:12px;font-weight:600;display:flex;align-items:center;justify-content:center;gap:8px}

/* feature tiles */
.tile{top:727px;width:336px;height:243px;overflow:hidden}
.tile .photo{width:100%;height:100%}
.tile .caption{position:absolute;left:0;bottom:0;width:100%;height:70px;background:rgba(35,35,35,.78);color:#fff;font-family:"Fira Sans",Arial,sans-serif;font-size:24px;display:flex;align-items:center;padding-left:22px}

/* services */
.services{top:1048px;left:0;width:1200px;height:526px;background:var(--light)}
.service{width:300px}
.service svg{position:absolute;left:0;top:0}
.service h3{position:absolute;left:66px;top:0;font-family:"Fira Sans",Arial,sans-serif;font-size:15px;font-weight:600;color:#333;white-space:nowrap}
.service p{position:absolute;left:66px;top:24px;width:240px;font-size:12px;line-height:20px;color:#555}

/* quote band */
.quote-band{top:1574px;left:0;width:1200px;height:214px;background:var(--band)}
.quote-band p{position:absolute;left:0;width:1200px;text-align:center;font-family:"Fira Sans",Arial,sans-serif;font-weight:600;font-size:28px;letter-spacing:1.5px}

/* news */
.news-card{top:1975px;height:268px}
.news-card .text{position:absolute;left:0;top:0;width:275px;height:240px;background:#ebebeb;padding:66px 26px 0}
.news-card h4{font-family:"Fira Sans",Arial,sans-serif;font-weight:400;font-size:17px;color:#3b5f8f;margin-bottom:14px}
.news-card .excerpt{font-size:13px;line-height:24px;color:#8a9bb0}
.news-card .more{margin-top:18px;font-size:12px;color:#3b5f8f}
.news-card .photo{position:absolute;left:275px;top:0;width:253px;height:268px}
.news-card .date{position:absolute;left:275px;top:0;width:64px;height:62px;background:#555;color:#fff;font-size:11px;line-height:14px;text-align:center;padding-top:18px;font-weight:600}
.dots{top:2301px;left:570px;display:flex;gap:8px}
.dots span{width:16px;height:16px;border-radius:50%;background:#9a9a9a}
.dots span.on{background:var(--accent)}

/* solutions */
.solutions{top:2370px;left:0;width:1200px;height:565px;background:linear-gradient(180deg,#2c2c2c,#3a3a3a 60%,#2e2e2e)}
.solution .photo{position:absolute;left:0;top:0;width:343px;height:192px}
.solution h3{position:absolute;left:0;top:210px;font-family:"Fira Sans",Arial,sans-serif;font-weight:600;font-size:21px;color:#fff;white-space:nowrap}
.solution p{position:absolute;left:0;top:244px;width:343px;font-size:12.5px;line-height:20px;color:#e4e4e4;text-align:justify}
.solution .btn{position:absolute;left:0;top:338px;width:104px;height:38px;border:2px solid #ddd;color:#fff;font-size:13px;display:flex;align-items:center;justify-content:center}

/* testimonials */
.testimonial-text{top:3138px;left:150px;width:900px;text-align:center;font-style:italic;font-size:13px;line-height:26px;color:#777}
.by{top:3236px;left:0;width:1200px;text-align:center;font-size:11px;color:#999}
.author{top:3262px;left:0;width:1200px;text-align:center;font-size:13px;font-weight:600;color:#333}

/* footer */
.footer{top:3483px;left:0;width:1200px;height:306px;background:var(--darker)}
.footer .links{position:absolute;top:137px;left:0;width:1200px;text-align:center;color:#fff;font-size:14px;letter-spacing:.5px}
.footer .copy{position:absolute;top:167px;left:0;width:1200px;text-align:center;color:#fff;font-size:14px}
.footer .social{position:absolute;top:222px;left:510px;display:flex;gap:20px}
.footer .social span{width:30px;height:30px;background:#fff;transform:rotate(45deg);margin:4px}
</style>
</head>
<body>
<div class="page">

  <!-- top bar -->
  <div class="abs topbar">
    <div class="item" style="left:88px">English <span style="font-size:9px">▼</span></div>
    <div class="item" style="left:196px">
      <svg width="12" height="16" viewBox="0 0 12 16"><path d="M6 0a6 6 0 0 0-6 6c0 4.5 6 10 6 10s6-5.5 6-10a6 6 0 0 0-6-6z" fill="#ccc"/><circle cx="6" cy="6" r="2.2" fill="#262626"/></svg>
      240 Harrow Lane, New York, NY 10022 US.
    </div>
    <div class="item" style="left:574px">
      <svg width="14" height="14" viewBox="0 0 14 14"><circle cx="7" cy="7" r="6" fill="none" stroke="#ccc" stroke-width="1.5"/><path d="M7 3.5V7h3" fill="none" stroke="#ccc" stroke-width="1.5"/></svg>
      Mon - Sat 8.00 - 18.00. Sunday CLOSED
    </div>
    <div class="item" style="left:862px">
      <svg width="14" height="14" viewBox="0 0 14 14"><path d="M3 1l2.5 3-1.5 1.5c.8 1.8 2.2 3.2 4 4L9.5 8 13 10.5 11.5 13C6 12.5 1.5 8 1 2.5z" fill="#ccc"/></svg>
      212 555 0148
    </div>
    <div class="item city">NEW YORK <span style="font-size:9px">▼</span></div>
  </div>

  <!-- hero -->
  <div class="abs hero" role="img" aria-label="Photo of two business consultants in suits smiling while reviewing work at a desk"></div>
  <div class="abs navbar"></div>
  <div class="abs brand-mark"></div>
  <div class="abs brand-name">MARLOW VANE</div>
  <nav class="abs nav">
    <a class="active" href="#">HOME</a>
    <a href="#">ABOUT US</a>
    <a href="#">SERVICES</a>
    <a href="#">CONTACT US</a>
  </nav>
  <div class="abs cta-strip">
    <p>Looking for a First-Class Business Consultant?</p>
    <div class="btn">get a qoute
      <svg width="8" height="12" viewBox="0 0 8 12"><path d="M1.5 1l5 5-5 5" fill="none" stroke="#fff" stroke-width="2"/></svg>
    </div>
  </div>

  <!-- feature tiles -->
  <div class="abs tile" style="left:56px">
    <div class="photo" role="img" aria-label="Photo of a hand writing with a pen on documents" style="background:linear-gradient(135deg,#e8e8e8,#9aa0a8 60%,#4b4f58)"></div>
    <div class="caption">What we Do</div>
  </div>
  <div class="abs tile" style="left:429px">
    <div class="photo" role="img" aria-label="Photo of a team of colleagues gathered around a laptop" style="background:linear-gradient(135deg,#f1f1f1,#b5aca2 55%,#5c6270)"></div>
    <div class="caption">We know</div>
  </div>
  <div class="abs tile" style="left:803px">
    <div class="photo" role="img" aria-label="Photo of a business meeting with papers and laptops on a table" style="background:linear-gradient(135deg,#dfe5ec,#9fb0c4 55%,#5d6a7d)"></div>
    <div class="caption">Touch</div>
  </div>

  <!-- services -->
  <section class="abs services">
    <h2 class="heading" style="top:30px;font-size:34px;color:#333">Our Services</h2>

    <div class="abs service" style="left:63px;top:148px">
      <svg width="50" height="50" viewBox="0 0 50 50"><circle cx="25" cy="25" r="22" fill="none" stroke="#666" stroke-width="2"/><circle cx="25" cy="25" r="11" fill="none" stroke="#666" stroke-width="2"/><path d="M14 25h22M25 14v22" stroke="#666" stroke-width="1.5"/></svg>
      <h3>Business Strategy</h3>
      <p>Company that offers design and build services for you from initial sketches to the final production.</p>
    </div>
    <div class="abs service" style="left:462px;top:148px">
      <svg width="50" height="50" viewBox="0 0 50 50"><circle cx="25" cy="25" r="22" fill="#666"/><circle cx="25" cy="25" r="16" fill="#fff"/><rect x="16" y="19" width="18" height="12" fill="#666"/></svg>
      <h3>Executive Coaching</h3>
      <p>Company that offers design and build services for you from initial sketches to the final production.</p>
    </div>
    <div class="abs service" style="left:831px;top:148px">
      <svg width="50" height="50" viewBox="0 0 50 50"><circle cx="25" cy="25" r="22" fill="none" stroke="#666" stroke-width="2"/><rect x="17" y="14" width="16" height="22" fill="none" stroke="#666" stroke-width="2"/><path d="M20 20h10M20 25h10M20 30h6" stroke="#666" stroke-width="1.5"/></svg>
      <h3>Corporate Governance</h3>
      <p>Company that offers design and build services for you from initial sketches to the final production.</p>
    </div>
    <div class="abs service" style="left:63px;top:340px">
      <svg width="50" height="50" viewBox="0 0 50 50"><circle cx="25" cy="25" r="22" fill="#666"/><path d="M15 33l7-8 5 4 8-12" fill="none" stroke="#fff" stroke-width="2.5"/></svg>
      <h3>Performance Management</h3>
      <p>Company that offers design and build services for you from initial sketches to the final production.</p>
    </div>
    <div class="abs service" style="left:462px;top:340px">
      <svg width="50" height="50" viewBox="0 0 50 50"><circle cx="25" cy="25" r="22" fill="none" stroke="#666" stroke-width="2"/><circle cx="25" cy="20" r="5" fill="#666"/><path d="M15 34c2-6 18-6 20 0z" fill="#666"/></svg>
      <h3>New Business Development</h3>
      <p>Company that offers design and build services for you from initial sketches to the final production.</p>
    </div>
    <div class="abs service" style="left:831px;top:340px">
      <svg width="50" height="50" viewBox="0 0 50 50"><circle cx="25" cy="25" r="22" fill="#666"/><rect x="14" y="16" width="22" height="15" fill="none" stroke="#fff" stroke-width="2"/><path d="M20 36h10" stroke="#fff" stroke-width="2"/></svg>
      <h3>Risk Management</h3>
      <p>Company that offers design and build services for you from initial sketches to the final production.</p>
    </div>
  </section>

  <!-- quote band -->
  <section class="abs quote-band">
    <p style="top:58px;color:#8c8c8c">TO HELP ENTREPRENEURS GET THEIR ACT TOGETHER</p>
    <p style="top:105px;color:#fff">BEFORE THEY TALK TO INVESTORS.</p>
  </section>

  <!-- news -->
  <h2 class="heading" style="top:1840px;font-size:34px;color:#333">NEWS</h2>
  <div class="abs" style="top:1892px;left:560px;width:80px;height:3px;background:#333"></div>

  <article class="abs news-card" style="left:56px;width:528px">
    <div class="text">
      <h4>News Heading</h4>
      <p class="excerpt">There are many variations of passages of Lorem Ipsum available majority have suffered...</p>
      <p class="more">Read More ⟶</p>
    </div>
    <div class="photo" role="img" aria-label="Photo of colleagues discussing ideas at a glass board" style="background:linear-gradient(135deg,#f0f0f0,#c5cdd6 55%,#7a8594)"></div>
    <div class="date">29<br>NOV</div>
  </article>
  <article class="abs news-card" style="left:616px;width:528px">
    <div class="text">
      <h4>News Heading</h4>
      <p class="excerpt">If people are really excited about their music, and that's their primary motivation,...</p>
      <p class="more">Read More ⟶</p>
    </div>
    <div class="photo" role="img" aria-label="Photo of two businessmen shaking hands" style="background:linear-gradient(135deg,#eef2f6,#9cadc2 50%,#3d4e68)"></div>
    <div class="date">29<br>NOV</div>
  </article>
  <div class="abs dots"><span class="on"></span><span></span><span></span></div>

  <!-- solutions -->
  <section class="abs solutions">
    <h2 class="heading" style="top:28px;font-size:34px;color:#fff">Solutions</h2>

    <div class="abs solution" style="left:48px;top:131px">
      <div class="photo" role="img" aria-label="Photo of a man on the phone working at a laptop in a bright office" style="background:linear-gradient(135deg,#f4f4f4,#d9dadc 60%,#a7aab0)"></div>
      <h3>Our History</h3>
      <p>Our Offshore Development Center at Hyderabad, India is comprised of an excellent delivery facility and staff dedicated to our customer's IT requirements. The center consists of a team...</p>
      <div class="btn">Read More</div>
    </div>
    <div class="abs solution" style="left:429px;top:131px">
      <div class="photo" role="img" aria-label="Photo of a man working at a laptop at his desk" style="background:linear-gradient(135deg,#f2f2f2,#d0cfcc 60%,#9b9994)"></div>
      <h3>Our Clients</h3>
      <p>Our Offshore Development Center at Hyderabad, India is comprised of an excellent delivery facility and staff dedicated to our customer's IT requirements. The center consists of a team...</p>
      <div class="btn">Read More</div>
    </div>
    <div class="abs solution" style="left:811px;top:131px">
      <div class="photo" role="img" aria-label="Photo of a businesswoman seated at a laptop in a white office" style="background:linear-gradient(135deg,#fafafa,#e2e3e5 60%,#b4b8bf)"></div>
      <h3>What You Get</h3>
      <p>Our Offshore Development Center at Hyderabad, India is comprised of an excellent delivery facility and staff dedicated to our customer's IT requirements. The center consists of a team...</p>
      <div class="btn">Read More</div>
    </div>
  </section>

  <!-- testimonials -->
  <h2 class="heading" style="top:2962px;font-size:34px;color:#333">Tesimonials</h2>
  <svg class="abs" style="top:3054px;left:564px" width="72" height="56" viewBox="0 0 72 56">
    <path d="M0 28h24M48 28h24" stroke="#ccc" stroke-width="1"/>
    <circle cx="36" cy="28" r="20" fill="none" stroke="#999" stroke-width="1.5"/>
    <path d="M29 32a4 4 0 1 1 4-4c0 4-2 6-4 7M38 32a4 4 0 1 1 4-4c0 4-2 6-4 7" fill="none" stroke="#666" stroke-width="2"/>
  </svg>
  <p class="abs testimonial-text">Lorem Ipsum is simply dummy text of the printing and typesetting industry. Lorem Ipsum has been the industry's standard dummy text ever since the 1500s, when an unknown printer took a galley of type and scrambled it to make a type specimen book. It has survived not only five centuries, but also the leap into electronic typesetting, remaining essentially unchanged.</p>
  <p class="abs by">by</p>
  <p class="abs author">DR. CORWIN</p>
  <svg class="abs" style="top:3306px;left:505px" width="190" height="112" viewBox="0 0 190 112">
    <g role="img" aria-label="Client portrait">
      <polygon points="32,2 56,16 56,42 32,56 8,42 8,16" fill="#8a8a8a"/>
    </g>
    <g role="img" aria-label="Client portrait">
      <polygon points="94,2 118,16 118,42 94,56 70,42 70,16" fill="#d9763f"/>
    </g>
    <g role="img" aria-label="Client portrait">
      <polygon points="156,2 180,16 180,42 156,56 132,42 132,16" fill="#6e6e6e"/>
    </g>
    <g role="img" aria-label="Client portrait">
      <polygon points="63,56 87,70 87,96 63,110 39,96 39,70" fill="#b9a89a"/>
    </g>
    <g role="img" aria-label="Client portrait">
      <polygon points="125,56 149,70 149,96 125,110 101,96 101,70" fill="#c9875a"/>
    </g>
  </svg>

  <!-- footer -->
  <footer class="abs footer">
    <div class="abs" style="top:28px;left:514px;width:92px;height:92px;border-radius:50%;background:#fff"></div>
    <div class="abs" style="top:62px;left:618px;color:#fff;font-family:'Fira Sans',Arial,sans-serif;font-weight:600;font-size:18px;letter-spacing:1px">MARLOW VANE</div>
    <p class="links">HOME • SOLUTIONS • SERVICES • COMPANY • CONTACT</p>
    <p class="copy">Copyright © 2007 - 2015 www.marlowvane.co, Inc. All Rights Reserved</p>
    <div class="social"><span></span><span></span><span></span><span></span></div>
  </footer>

</div>
</body>
</html>
```